Evertide Planting Works and Tender-Shoot Emporium

The billboard will be on highway frontage and located directly next to my business building the marketing is for. The marketing on the billboard will be more directed towards the micro-greens superstore service being provided. And since the sign is on the businesses property it will need to say, "Exit Right Now" along with an arrow pointing to the right when facing the sign.

```html
<!DOCTYPE html>
<html lang="en">
<head>
<meta charset="utf-8">
<title>Evertide Planting Works – Highway Billboard</title>
<link rel="stylesheet" href="https://fonts.googleapis.com/css2?family=Montserrat:wght@700;800&display=swap">
<style>
  :root {
    --backdrop: #e9ecef;
    --board-black: #161616;
    --leaf-green: #8cc63f;
    --gold: #d6a955;
    --greens-dark: #3f5a2c;
    --greens-mid: #6f9a3e;
    --wood-grey: #5b5a55;
  }
  html, body {
    margin: 0;
    padding: 0;
    width: 1200px;
    height: 800px;
    overflow: hidden;
    background: var(--backdrop);
  }
  .billboard {
    position: absolute;
    left: 40px;
    top: 200px;
    width: 1120px;
    height: 400px;
    overflow: hidden;
    background: var(--board-black);
  }
  .billboard__art {
    position: absolute;
    inset: 0;
    width: 100%;
    height: 100%;
  }
  .brand {
    position: absolute;
    left: 46px;
    top: 150px;
    display: flex;
    align-items: center;
    gap: 14px;
    font-family: "Montserrat", sans-serif;
    font-weight: 700;
    color: var(--leaf-green);
    font-size: 28px;
    line-height: 1.15;
    letter-spacing: 0.5px;
  }
  .brand__dot {
    width: 26px;
    height: 26px;
    border-radius: 50%;
    background: var(--leaf-green);
    flex: none;
  }
  .callout {
    position: absolute;
    left: 392px;
    top: 82px;
    margin: 0;
    font-family: "Montserrat", sans-serif;
    font-weight: 800;
    color: var(--gold);
    font-size: 80px;
    line-height: 0.98;
    letter-spacing: -1px;
    text-transform: uppercase;
  }
  .callout span { display: block; }
</style>
</head>
<body>
  <div class="billboard">
    <svg class="billboard__art" viewBox="0 0 1120 400" aria-hidden="false">
      <defs>
        <linearGradient id="greensPhoto" x1="0" y1="0" x2="1" y2="1">
          <stop offset="0" stop-color="var(--greens-mid)"/>
          <stop offset="0.45" stop-color="var(--wood-grey)"/>
          <stop offset="1" stop-color="var(--greens-dark)"/>
        </linearGradient>
      </defs>
      <rect class="photo-area" x="500" y="0" width="620" height="400" fill="url(#greensPhoto)"
            role="img" aria-label="Overhead photo of microgreen trays and a letter board on a wooden table"/>
      <polygon class="arrow-accent" points="0,0 560,0 735,205 560,400 0,400" fill="var(--leaf-green)"/>
      <polygon class="arrow-body" points="0,0 540,0 712,205 545,400 0,400" fill="var(--board-black)"/>
    </svg>

    <div class="brand">
      <span class="brand__dot"></span>
      <span class="brand__name">Evertide<br>Planting Works</span>
    </div>

    <h1 class="callout"><span>Exit</span><span>Right</span><span>Now</span></h1>
  </div>
</body>
</html>
```